Brightloom Orthodontics business card design

Need a business card design that reflects our re-branding (orthodontic office - braces) and a new partnership with a pediatric dental office. We would like to include "for adults and children" on the card as well so adults know they are welcome to get their braces here as well. Office design is modern and would like business card to reflect a modern type look. Here's the text we would like to be included on the card:

Daniel Pruvost, DDS, MSD
5214 West Halden Avenue, Suite 204
Mansfield, TX 76099
682-555-4817
www.brightloomortho.example
info@brightloomortho.example
Updates

Can we add the following to the existing designs? Daniel Pruvost, DDS, MSD 5214 West Halden Avenue, Suite 204 Mansfield, TX 76099 682-555-4817

Does anyone have any more vertical designs available? Thanks!

Industry/Entity Type

Dental

```html
<!DOCTYPE html>
<html lang="en">
<head>
<meta charset="utf-8">
<title>Brightloom Orthodontics – Business Card</title>
<link rel="stylesheet" href="https://fonts.googleapis.com/css2?family=Open+Sans:ital,wght@0,400;0,600;0,700;1,400;1,600&display=swap">
<style>
  :root {
    --page: #ecebe8;
    --card: #ffffff;
    --ink: #262626;
    --muted: #5a5a5a;
    --rule: #cfcfcf;
    --brand-blue: #2b7fc8;
    --band: #1f1f1f;
    --sq-yellow: #f7e815;
    --sq-blue: #1e78c2;
    --sq-magenta: #e3138c;
    --sq-green: #8cc63f;
    --sq-orange: #f7941d;
  }
  * { box-sizing: border-box; margin: 0; padding: 0; }
  html, body {
    width: 1200px; height: 900px; overflow: hidden;
    background: var(--page);
    font-family: "Open Sans", Arial, sans-serif;
    color: var(--ink);
  }
  .card {
    position: absolute; left: 250px;
    width: 700px; height: 400px;
    background: var(--card);
    border-radius: 22px;
    overflow: hidden;
    box-shadow: 0 6px 18px rgba(0,0,0,.18);
  }
  .card--appointment { top: 35px; }
  .card--contact { top: 465px; }

  /* shared brand mark */
  .brand { position: absolute; display: flex; align-items: center; gap: 12px; }
  .brand__dot { width: 26px; height: 26px; border-radius: 50%; background: var(--brand-blue); flex: none; }
  .brand__name { font-weight: 700; color: var(--ink); line-height: 1.05; }

  /* colour strip */
  .strip { position: absolute; display: flex; height: 40px; }
  .strip span { display: block; height: 100%; }
  .sq-yellow { background: var(--sq-yellow); }
  .sq-blue { background: var(--sq-blue); }
  .sq-magenta { background: var(--sq-magenta); }
  .sq-green { background: var(--sq-green); }
  .sq-orange { background: var(--sq-orange); }
  .band { position: absolute; height: 40px; background: var(--band); color: #fff; display: flex; align-items: center; }

  /* appointment side */
  .appt__pill {
    position: absolute; left: 40px; top: 30px;
    background: var(--brand-blue); color: #fff;
    font-weight: 600; font-size: 19px;
    padding: 6px 22px; border-radius: 12px;
  }
  .field-label { position: absolute; color: var(--brand-blue); font-size: 15px; font-style: italic; }
  .field-line { position: absolute; height: 1px; background: #555; }
  .days { position: absolute; left: 40px; top: 218px; display: flex; gap: 30px; }
  .day { display: flex; align-items: center; gap: 7px; color: var(--brand-blue); font-size: 14px; }
  .day__box { width: 13px; height: 13px; border: 1px solid #666; background: #fff; }
  .ampm { position: absolute; right: 40px; top: 248px; color: var(--brand-blue); font-size: 12px; }
  .band--web { left: 250px; right: 0; bottom: 30px; justify-content: flex-end; padding-right: 40px; font-size: 15px; letter-spacing: 1px; }

  /* contact side */
  .divider { position: absolute; left: 372px; top: 80px; width: 1px; height: 180px; background: var(--rule); }
  .info { position: absolute; left: 398px; top: 78px; }
  .info__name { color: var(--brand-blue); font-weight: 700; font-size: 25px; line-height: 1.1; }
  .info__creds { color: var(--brand-blue); font-weight: 600; font-size: 18px; margin-bottom: 14px; }
  .info__address { color: var(--muted); font-size: 14.5px; line-height: 1.4; margin-bottom: 10px; }
  .info__row { display: flex; align-items: center; gap: 9px; color: var(--muted); font-size: 14.5px; line-height: 1.7; }
  .info__row svg { width: 16px; height: 16px; flex: none; }
  .band--tagline { left: 0; width: 390px; bottom: 50px; padding-left: 40px; font-size: 17px; font-style: italic; }
</style>
</head>
<body>

<section class="card card--appointment" aria-label="Appointment reminder side">
  <div class="appt__pill">Next Appointment</div>

  <span class="field-label" style="left:40px; top:78px;">Name :</span>
  <span class="field-line" style="left:100px; top:98px; width:340px;"></span>

  <span class="field-label" style="left:40px; top:150px;">Date :</span>
  <span class="field-line" style="left:95px; top:170px; width:565px;"></span>

  <div class="brand" style="right:40px; top:62px;">
    <span class="brand__dot"></span>
    <span class="brand__name" style="font-size:24px;">Brightloom<br>Orthodontics</span>
  </div>

  <div class="days">
    <span class="day"><span class="day__box"></span>Mon</span>
    <span class="day"><span class="day__box"></span>Tue</span>
    <span class="day"><span class="day__box"></span>Wed</span>
    <span class="day"><span class="day__box"></span>Thu</span>
    <span class="day"><span class="day__box"></span>Fri</span>
  </div>

  <span class="field-label" style="left:470px; top:208px;">Time :</span>
  <span class="field-line" style="left:470px; top:240px; width:190px;"></span>
  <span class="ampm">AM/PM</span>

  <div class="strip" style="left:0; bottom:30px;">
    <span class="sq-orange" style="width:50px;"></span>
    <span class="sq-green" style="width:50px;"></span>
    <span class="sq-magenta" style="width:50px;"></span>
    <span class="sq-blue" style="width:50px;"></span>
    <span class="sq-yellow" style="width:50px;"></span>
  </div>
  <div class="band band--web">www.brightloomortho.example</div>
</section>

<section class="card card--contact" aria-label="Contact side">
  <div class="brand" style="left:40px; top:110px;">
    <span class="brand__dot"></span>
    <span class="brand__name" style="font-size:34px;">Brightloom<br>Orthodontics</span>
  </div>

  <span class="divider"></span>

  <div class="info">
    <p class="info__name">Daniel Pruvost</p>
    <p class="info__creds">DDS, MSD</p>
    <p class="info__address">5214 West Halden Avenue, Suite 204<br>Mansfield, TX 76099</p>
    <p class="info__row">
      <svg viewBox="0 0 16 16" aria-hidden="true"><path fill="#2b7fc8" d="M3.5 1.5l2.5 2.6-1.3 1.8c.8 1.9 2.4 3.5 4.4 4.4l1.8-1.3 2.6 2.5-1.4 2.5C6.8 13.8 2.2 9.2 1 3z"/></svg>
      682-555-4817
    </p>
    <p class="info__row">
      <svg viewBox="0 0 16 16" aria-hidden="true"><rect x="1" y="3" width="14" height="10" rx="1" fill="#2b7fc8"/><path d="M1.5 3.6L8 9l6.5-5.4" fill="none" stroke="#fff" stroke-width="1.3"/></svg>
      info@brightloomortho.example
    </p>
    <p class="info__row">
      <svg viewBox="0 0 16 16" aria-hidden="true"><circle cx="8" cy="8" r="7" fill="#2b7fc8"/><g fill="none" stroke="#fff" stroke-width="1"><ellipse cx="8" cy="8" rx="3" ry="7"/><path d="M1 8h14M2.5 4.5h11M2.5 11.5h11"/></g></svg>
      www.brightloomortho.example
    </p>
  </div>

  <div class="band band--tagline">For children and adults</div>
  <div class="strip" style="left:390px; right:0; bottom:50px;">
    <span class="sq-yellow" style="width:62px;"></span>
    <span class="sq-blue" style="width:62px;"></span>
    <span class="sq-magenta" style="width:62px;"></span>
    <span class="sq-green" style="width:62px;"></span>
    <span class="sq-orange" style="width:62px;"></span>
  </div>
</section>

</body>
</html>
```